Thank You For Shopping / Hair Care Tips

I need “Thank You For Shopping”
Post cards made for my hair business !
I added pictures of post cards that I really like . I also added my LunaVex Wigs logo for you guys to use

I want the backside of the flyer to have hair care tips !
I want people to have full directions on how to care for their wigs

Target Market(s)

Im marking to young woman to older middle aged woman
Ages 23-66 . I want my flyer to look mature And classy

Industry/Entity Type

Hair And Beauty

Font styles to use
Serif
Script

Colors
e34699
e34298
e34398

Requirements
Must have
• The flyer must have the Instagram logo with my Instagram name next to it @luna.vex.wigs__
• Also it must have my “Luna Vex Wigs” logo that I’ve uploaded in the pictures section .
• Flyer had to be two sides . One side “ thank you for shopping “ side two “hair care tips”
• My website must be on the flyer - www.lunavexwigs.example
• The flyer must match the colors of my logo
• All white . With the pink and glitter sliver you see on my logo
Nice to have
• Nice to have a glitter border
Should not have
• The flyer should not have different colors that don’t match my logo
• It shouldn’t be made without having my Instagram or website on the flyer

```html
<!DOCTYPE html>
<html lang="en">
<head>
<meta charset="utf-8">
<title>LunaVex Wigs – Thank You Postcard</title>
<link rel="stylesheet" href="https://fonts.googleapis.com/css2?family=Pinyon+Script&family=Playfair+Display:wght@600&family=Poppins:wght@300;400&display=swap">
<style>
  :root {
    --pink: #e34699;
    --silver: #a9a9ad;
    --silver-dark: #6f6f74;
    --ink: #3c3c40;
    --paper: #ffffff;
    --page: #f2f2f3;
  }
  * { box-sizing: border-box; margin: 0; padding: 0; }
  html, body { width: 672px; height: 1200px; overflow: hidden; }
  body {
    background: var(--page);
    position: relative;
    font-family: "Poppins", sans-serif;
    color: var(--ink);
  }
  .side-label {
    position: absolute;
    left: 24px;
    font-family: "Pinyon Script", cursive;
    font-size: 68px;
    line-height: 1;
    color: var(--pink);
  }
  .side-label--front { top: 14px; }
  .side-label--back { top: 580px; }

  .postcard {
    position: absolute;
    left: 36px;
    width: 600px;
    height: 460px;
    background: var(--paper);
    border: 8px solid var(--silver);
    box-shadow: 0 4px 14px rgba(0,0,0,.12);
  }
  .postcard::before {
    content: "";
    position: absolute;
    inset: 7px;
    border: 1.5px solid var(--silver);
    pointer-events: none;
  }
  .postcard--front { top: 100px; }
  .postcard--back { top: 670px; }

  .corner {
    position: absolute;
    width: 14px;
    height: 14px;
    border: 1.5px solid var(--silver);
    background: var(--paper);
  }
  .corner--tl { top: 2px; left: 2px; }
  .corner--tr { top: 2px; right: 2px; }
  .corner--bl { bottom: 2px; left: 2px; }
  .corner--br { bottom: 2px; right: 2px; }

  /* Front */
  .thanks {
    position: absolute;
    top: 62px;
    left: 0;
    right: 0;
    text-align: center;
    font-family: "Pinyon Script", cursive;
    font-size: 46px;
    color: var(--silver-dark);
  }
  .brand-name {
    position: absolute;
    top: 170px;
    left: 0;
    right: 0;
    text-align: center;
    font-family: "Playfair Display", serif;
    font-weight: 600;
    font-size: 52px;
    letter-spacing: 2px;
    color: var(--pink);
  }
  .contact-list {
    position: absolute;
    left: 140px;
    top: 300px;
    list-style: none;
  }
  .contact-list li {
    display: flex;
    align-items: center;
    gap: 12px;
    margin-bottom: 10px;
    font-size: 17px;
    letter-spacing: .5px;
    color: var(--pink);
    text-transform: uppercase;
  }
  .contact-icon { flex: none; }

  /* Back */
  .tips-title {
    text-align: center;
    font-family: "Pinyon Script", cursive;
    font-size: 50px;
    line-height: 1;
    color: var(--pink);
    margin-top: 26px;
  }
  .tips {
    padding: 12px 22px 0 26px;
    font-size: 9.6px;
    line-height: 1.55;
  }
  .tips ul { list-style: none; }
  .tips li {
    position: relative;
    padding-left: 12px;
  }
  .tips li::before {
    content: "";
    position: absolute;
    left: 0;
    top: 5px;
    width: 5px;
    height: 5px;
    border-radius: 50%;
    background: var(--pink);
  }
  .tips-heading {
    margin: 8px 0 2px 10px;
    font-size: 11px;
    font-weight: 400;
    text-transform: uppercase;
  }
</style>
</head>
<body>

  <div class="side-label side-label--front">Front</div>

  <section class="postcard postcard--front" aria-label="Postcard front">
    <span class="corner corner--tl"></span><span class="corner corner--tr"></span>
    <span class="corner corner--bl"></span><span class="corner corner--br"></span>

    <p class="thanks">Thank You For Shopping</p>
    <p class="brand-name">Luna Vex Wigs</p>

    <ul class="contact-list">
      <li>
        <svg class="contact-icon" width="22" height="22" viewBox="0 0 22 22" aria-hidden="true">
          <circle cx="11" cy="11" r="10" fill="none" stroke="#6f6f74" stroke-width="2"/>
        </svg>
        www.lunavexwigs.example
      </li>
      <li>
        <svg class="contact-icon" width="22" height="22" viewBox="0 0 22 22" aria-hidden="true">
          <circle cx="11" cy="11" r="10" fill="none" stroke="#6f6f74" stroke-width="2"/>
        </svg>
        @luna.vex.wigs__
      </li>
    </ul>
  </section>

  <div class="side-label side-label--back">Back</div>

  <section class="postcard postcard--back" aria-label="Postcard back">
    <span class="corner corner--tl"></span><span class="corner corner--tr"></span>
    <span class="corner corner--bl"></span><span class="corner corner--br"></span>

    <h1 class="tips-title">Hair Care Tips</h1>

    <div class="tips">
      <ul>
        <li>Apply a moisture rich Conditioner and comb hair, starting with the ends working your way up to your scalp.</li>
        <li>Leave Conditioner in for at least 15 minutes or more</li>
        <li>Do not massage the hair.</li>
        <li>Rinse thoroughly.</li>
        <li>Scrunch hair gently to enhance the curls. (For wavy/curly patterns)</li>
        <li>When damp, apply a dime size of an frizz alcohol free hair serum.</li>
        <li>Let air dry</li>
        <li>Do not use all products or excessive products on curly hair, it will cause matting.</li>
        <li>Do not brush or comb hair when dry, it will cause hair to frizz and may cause hair to tangle.</li>
      </ul>
      <h2 class="tips-heading">Bed Time Care</h2>
      <ul>
        <li>Before going to bed, braid your hair into one loose large braid and wear a satin scarf or bonnet.</li>
        <li>After waking up, undo braid and comb using a wild tooth comb (for paddle brush/ through beginning at the ends and working your way up to roots.</li>
        <li>style as needed</li>
      </ul>
    </div>
  </section>

</body>
</html>
```